New Website Design for PALVO.org

We are looking for a new website design for PALVO.org. PALVO is a non profit home inspector association based in California. Home Inspectors are people that come out and look at a house before it's purchased to let the buyer know of any defects that may exist.
Our site is based on Joomla so if you'll be able to make a Joomla 3 template as well, please let us know (not required, but a bonus).
We would like to see designs that incorporate royal blue, white and chrome into the site as that's our main business colors.
We would like a place for rotating banners though they don't need to be the same size as the current site.
We would like navigation to be easier to manage with menus only across the top (via drop down menus) where we are going to sort out the items currently on the side. Possibly the front page could have a graphic link to separate portals for Realtors, Home Buyers and Inspectors, but that's just one option.
We would like a good mobile design or something that will scale easily to mobile.
The Find an Inspector feature is important and should stand out. The ZIM PALVOr site
Current home page feels a bit busy. Would like to simplify a bit.

```html
<!DOCTYPE html>
<html lang="en">
<head>
<meta charset="utf-8">
<title>PALVO – California Property Valuation Alliance</title>
<link href="https://fonts.googleapis.com/css2?family=Play:wght@400;700&family=Arimo:wght@700&display=swap" rel="stylesheet">
<style>
:root{
  --royal:#283d8c;
  --nav-top:#4a63b8;
  --nav-bot:#23378a;
  --ink:#333;
  --muted:#7a7a7a;
  --chrome:#f3f3f3;
  --icon:#1b1b1b;
  --black:#111;
}
*{box-sizing:border-box;margin:0;padding:0}
html,body{width:1003px;height:1200px;overflow:hidden}
body{position:relative;background:#fff;font-family:"Play",sans-serif;color:var(--ink)}
.abs{position:absolute}
.topline{left:0;top:0;width:1003px;height:4px;background:#3a3a3a}
.header{left:0;top:4px;width:1003px;height:105px;background:linear-gradient(#f6f6f6,#ececec)}
.brand-mark{left:121px;top:17px;width:80px;height:80px;border-radius:50%;border:4px solid #2b2b40;background:#e9ecf4;display:flex;align-items:center;justify-content:center;font-size:15px;font-weight:700;color:var(--royal)}
.brand-name{left:220px;top:34px;font-size:22px;line-height:24px;color:#1e1e1e;letter-spacing:.5px}
.account-tab{left:700px;top:0;width:170px;height:27px;background:#222;border-radius:0 0 4px 4px;color:#fff;font-size:12.5px;display:flex;align-items:center;justify-content:center;gap:12px}
.follow{left:695px;top:66px;font-size:13px;color:#222;letter-spacing:.5px}
.social{top:63px;width:18px;height:18px;border-radius:3px;background:#c9ccd4}
.nav{left:0;top:109px;width:1003px;height:40px;background:linear-gradient(var(--nav-top),var(--nav-bot));border-top:1px solid #7d90d0}
.nav a{position:absolute;top:11px;color:#fff;font-size:13px;text-decoration:none}
.hero{left:0;top:149px;width:1003px;height:378px;background:linear-gradient(100deg,#f2e3c8 0%,#e6c79a 30%,#f4efe6 55%,#e0c089 80%,#f3e7d2 100%)}
.caption{left:92px;top:317px;width:431px;height:109px;background:rgba(255,255,255,.85);border-radius:3px;padding:13px 18px}
.caption h1{font-family:"Arimo",sans-serif;font-size:26px;line-height:34px;letter-spacing:-2.1px;color:var(--royal);white-space:nowrap}
.caption p{font-size:13.5px;color:#333;margin-top:1px}
.panel{left:92px;top:442px;width:819px;height:530px;background:#fff;box-shadow:0 0 30px rgba(0,0,0,.12)}
.cards{left:92px;top:442px;width:819px;height:155px;background:var(--chrome);border-bottom:3px solid var(--royal)}
.card{top:0;height:152px;border-right:1px solid #e2e2e2}
.card svg{position:absolute;left:20px;top:18px}
.card h2{position:absolute;top:15px;font-weight:400;font-size:19px;color:var(--royal);letter-spacing:.5px}
.card p{position:absolute;top:42px;width:166px;font-size:11px;line-height:15px;color:#555}
.btn{display:inline-block;background:var(--royal);color:#fff;font-size:11.5px;font-weight:700;padding:2px 8px;letter-spacing:.3px}
.card .btn{position:absolute;top:122px}
.welcome-title{left:114px;top:618px;font-size:20px;font-weight:400;color:var(--royal)}
.welcome-text{left:115px;top:655px;width:516px;font-size:12px;line-height:19.2px;color:var(--muted)}
.site-photo{left:645px;top:624px;width:249px;height:122px;background:linear-gradient(90deg,#8a6a44,#c49b66 45%,#e4c9a2 70%,#a07a4e)}
.col-title{font-size:16px;color:var(--royal);font-weight:400;letter-spacing:.4px}
.search p{font-size:11px;line-height:16px;color:#444;margin:10px 0 12px;width:230px}
.zip{width:236px;height:26px;border:1px solid #ccc;border-top-color:#999;background:#fafafa;font-size:12.5px;color:#555;padding:5px 9px;margin-bottom:13px}
.news .item{font-size:11px;color:#444;line-height:13px;margin-top:11px}
.news .item span{display:block;font-size:10px;color:#555}
.testi{height:48px;position:relative;margin-top:10px}
.testi .avatar{position:absolute;left:0;top:0;width:48px;height:46px;background:linear-gradient(#e8e2dc,#a98b76)}
.testi .who{position:absolute;left:58px;top:0;font-size:11px;color:#333}
.testi .quote{position:absolute;left:58px;top:18px;width:192px;font-size:10.5px;line-height:14px;color:#555}
.testi .date{position:absolute;right:0;top:32px;font-size:9px;color:var(--royal)}
.footer{left:0;top:972px;width:1003px;height:188px;background:linear-gradient(#f3f3f3,#e4e4e4)}
.footer .col{position:absolute;top:26px}
.footer .link{font-size:10.5px;line-height:17.6px;color:#555}
.field{width:183px;height:20px;border:1px solid #ccc;background:#fff;border-radius:2px;font-size:10px;color:#999;padding:3px 11px;margin-top:8px}
.contact p{font-size:10.5px;line-height:14px;color:#444;margin-top:5px}
.bottom{left:0;top:1160px;width:1003px;height:40px;background:var(--black);color:#fff;font-size:10.5px}
.bottom .copy{position:absolute;left:104px;top:13px}
.bottom .links{position:absolute;right:104px;top:12px;display:flex;gap:11px}
</style>
</head>
<body>
<div class="abs topline"></div>
<header class="abs header"></header>
<div class="abs brand-mark">PALVO</div>
<div class="abs brand-name">California Property Valuation<br>Alliance</div>
<div class="abs account-tab"><span>Inspector Login</span><span>|</span><span>Sing Up</span></div>
<div class="abs follow">FOLLOW US</div>
<div class="abs social" style="left:782px" aria-label="Social link"></div>
<div class="abs social" style="left:808px" aria-label="Social link"></div>
<div class="abs social" style="left:834px" aria-label="Social link"></div>
<div class="abs social" style="left:860px" aria-label="Social link"></div>

<nav class="abs nav">
  <a style="left:104px">Home</a>
  <a style="left:177px">Find an Inspector</a>
  <a style="left:316px">Home Buyers &amp; Sellers</a>
  <a style="left:486px">Real Estate Agents</a>
  <a style="left:633px">Inspectors</a>
  <a style="left:733px">Ask PALVO</a>
  <a style="left:826px">Conferences</a>
</nav>

<div class="abs hero" role="img" aria-label="Photo of a home inspector in a hard hat and safety glasses inside a timber frame"></div>
<div class="abs caption">
  <h1>Lorem Ipsum est simplement du faux<br>texte employé dans sition.</h1>
  <p>Survivre cinq siècles, mais s'est aussi adapté</p>
</div>

<div class="abs panel"></div>
<section class="abs cards">
  <div class="abs card" style="left:0;width:273px">
    <svg width="48" height="48" viewBox="0 0 48 48" aria-hidden="true"><circle cx="24" cy="24" r="22" fill="none" stroke="var(--icon)" stroke-width="3"/><path d="M14 26 L24 16 L34 26 M18 23 V34 H30 V23" fill="none" stroke="var(--icon)" stroke-width="3" stroke-linejoin="round"/></svg>
    <h2 style="left:86px">Realtors</h2>
    <p style="left:87px">Lorem Ipsum est simplement du faux texte employé dans la sition et la misen page avant impression. Le Lorem Ipsum est le faux texte.</p>
    <span class="btn" style="left:87px">Find Retailer</span>
  </div>
  <div class="abs card" style="left:273px;width:273px">
    <svg width="48" height="48" viewBox="0 0 48 48" aria-hidden="true"><circle cx="24" cy="24" r="22" fill="none" stroke="var(--icon)" stroke-width="3"/><circle cx="24" cy="19" r="5" fill="none" stroke="var(--icon)" stroke-width="3"/><path d="M14 35 C14 28 34 28 34 35" fill="none" stroke="var(--icon)" stroke-width="3"/></svg>
    <h2 style="left:91px">Home Buyers</h2>
    <p style="left:92px">Lorem Ipsum est simplement du faux texte employé dans la sition et la misen page avant impression. Le Lorem Ipsum est le faux texte.</p>
    <span class="btn" style="left:92px">Find Buyer</span>
  </div>
  <div class="abs card" style="left:546px;width:273px;border-right:0">
    <svg width="48" height="48" viewBox="0 0 48 48" aria-hidden="true"><circle cx="24" cy="24" r="22" fill="none" stroke="var(--icon)" stroke-width="3"/><path d="M14 24 L21 31 L34 17" fill="none" stroke="var(--icon)" stroke-width="3.5" stroke-linecap="round" stroke-linejoin="round"/></svg>
    <h2 style="left:86px">Inspectors</h2>
    <p style="left:87px">Lorem Ipsum est simplement du faux texte employé dans la sition et la misen page avant impression. Le Lorem Ipsum est le faux texte.</p>
    <span class="btn" style="left:87px">Find Inspector</span>
  </div>
</section>

<h2 class="abs welcome-title">Welcome to California Property Valuation Alliance</h2>
<p class="abs welcome-text">Lorem Ipsum est simplement du faux texte employé dans la sition et la misen page avant impression. Le Lorem Ipsum est le faux texte standard de l'imprimerie depuis les années 1500, quand un peintre anonyme assembla ensemble des morceaux de texte pour réaliser un livre spécimen de polices de texte. mais s'est aussi adapté bureautique informatique, sans que son contenu n'en soit modifié. Popularisé dans les années 1960.</p>
<div class="abs site-photo" role="img" aria-label="Photo of inspectors checking the wooden framing of a house under construction"></div>

<section class="abs search" style="left:115px;top:794px">
  <h3 class="col-title">Search for Inspector</h3>
  <p>Lorem Ipsum est simplement du faux texte employé dans.</p>
  <div class="zip">Enter your Zip Code</div>
  <span class="btn">Search</span>
</section>

<section class="abs news" style="left:372px;top:794px">
  <h3 class="col-title">News &amp; Events</h3>
  <div class="item">Praesent luptatum ril delenit augue duis dolore<span>Yesterday at 08:23:14 PM</span></div>
  <div class="item">Praesent luptatum ril delenit augue duis dolore<span>Yesterday at 07:58:35 PM</span></div>
  <div class="item">Praesent luptatum ril delenit augue duis dolore<span>Yesterday at 07:11:19 PM</span></div>
</section>

<section class="abs" style="left:643px;top:794px;width:248px">
  <h3 class="col-title">Testimonials</h3>
  <div class="testi"><div class="avatar" role="img" aria-label="Portrait photo of the reviewer"></div><div class="who">Marlon Hadley</div><div class="quote">On sait depuis longtemps que travailler avec du texte lisibale</div><div class="date">14-12-2012</div></div>
  <div class="testi" style="margin-top:17px"><div class="avatar" role="img" aria-label="Portrait photo of the reviewer"></div><div class="who">Marlon Hadley</div><div class="quote">On sait depuis longtemps que travailler avec du texte lisibale</div><div class="date">14-12-2012</div></div>
</section>

<footer class="abs footer">
  <div class="col" style="left:105px">
    <h3 class="col-title">Inspector Login</h3>
    <div class="field" style="margin-top:13px">Username</div>
    <div class="field">Password</div>
    <span class="btn" style="margin-top:17px;padding:2px 10px">Login</span>
  </div>
  <div class="col" style="left:334px">
    <h3 class="col-title">SiteMap</h3>
    <div class="link" style="margin-top:6px">Praesent luptatum delen<br>it augue duis dolore<br>Praesent luptatum delen<br>it augue duis dolore<br>Praesent luptatum delen<br>it augue duis dolore</div>
  </div>
  <div class="col" style="left:522px">
    <h3 class="col-title">Other Items</h3>
    <div class="link" style="margin-top:6px">Praesent luptatum delen<br>it augue duis dolore<br>Praesent luptatum delen<br>it augue duis dolore<br>Praesent luptatum delen<br>it augue duis dolore</div>
  </div>
  <div class="col contact" style="left:697px">
    <h3 class="col-title">Contact Details</h3>
    <p>Contact details will be appear here<br>contact details here</p>
    <p style="margin-top:14px">Phone No. : 00 555 018-4420</p>
    <p style="margin-top:14px">E-mail : hello@palvo-mail.org</p>
  </div>
</footer>

<div class="abs bottom">
  <span class="copy">California Property Valuation Alliance. All Rights Reserved</span>
  <div class="links"><span>Find an Inspector</span><span>Home Buyers &amp; Sellers</span><span>Real Estate Agents</span></div>
</div>
</body>
</html>
```